Velvet Dare Age Verification Landing Page

To create a visually appealing design for the landing page of the adult game "Velvet Dare" that confirms the visitor's age.
The design should have a simple and visually appealing look that focuses on two buttons labeled "Yes" and "No". The purpose of the page is to confirm that the visitor is 18 years of age or older before accessing the game's content. Responsive design that works well on desktop and mobile devices. The final output should be delivered in PSD, AI, or Sketch format, along with any necessary images or assets.
I have also attached examples.

```html
<!DOCTYPE html>
<html lang="en">
<head>
<meta charset="utf-8">
<title>Velvet Dare – Age Verification</title>
<link rel="stylesheet" href="https://fonts.googleapis.com/css2?family=Roboto:wght@400;700&family=Almendra:wght@700&display=swap">
<style>
  :root{
    --ink:#ffffff;
    --muted:#a9a6ad;
    --frame:#8d8a92;
    --panel:#000000;
    --yes:#6338c4;
    --no:#2c1656;
    --brand:#c77dd8;
    --bg-deep:#070109;
  }
  *{margin:0;padding:0;box-sizing:border-box}
  html,body{width:1200px;height:853px;overflow:hidden;background:var(--bg-deep)}
  body{position:relative;font-family:'Roboto',sans-serif;color:var(--ink)}
  .backdrop{position:absolute;inset:0;
    background:
      radial-gradient(ellipse 260px 380px at 150px 420px, rgba(180,70,60,.55), transparent 70%),
      radial-gradient(ellipse 520px 180px at 820px 300px, rgba(170,0,40,.85), transparent 75%),
      radial-gradient(circle 120px at 1110px 160px, rgba(130,40,170,.7), transparent 75%),
      linear-gradient(180deg,#33084a 0%,#4a0a3a 25%,#6a0618 42%,#1a0208 58%,#050005 72%,#050005 100%);
  }
  .backdrop::after{content:"";position:absolute;left:0;top:0;width:440px;height:853px;
    background:linear-gradient(90deg,rgba(20,2,6,.6),rgba(150,10,10,.35) 85%,rgba(0,0,0,0));}
  .brand{position:absolute;left:487px;top:36px;width:110px;display:flex;align-items:center;gap:6px;
    font-family:'Roboto',sans-serif;font-weight:700;font-size:18px;color:var(--brand);white-space:nowrap}
  .brand-dot{width:12px;height:12px;border-radius:50%;background:var(--brand);flex:none}
  .welcome{position:absolute;left:487px;width:656px;top:162px;text-align:center;
    font-family:'Almendra',serif;font-weight:700;font-size:84px;line-height:1}
  .intro{position:absolute;left:480px;width:670px;top:265px;text-align:center;font-size:14.6px;line-height:21px}
  .age-check{position:absolute;left:518px;top:492px;width:599px;height:168px;background:var(--panel);
    border:2px solid var(--frame);border-radius:8px;padding:20px 0 0 40px}
  .age-check h1{font-size:25px;font-weight:700;line-height:32px}
  .choices{display:flex;gap:20px;margin-top:9px}
  .choice{height:37px;border:none;color:var(--ink);font:400 14.5px 'Roboto',sans-serif;letter-spacing:.3px}
  .choice.yes{width:192px;background:var(--yes)}
  .choice.no{width:198px;background:var(--no)}
  .notice{position:relative;margin-top:10px;padding-left:23px;width:520px;font-size:12.5px;line-height:18.5px;color:var(--muted)}
  .notice svg{position:absolute;left:2px;top:2px}
  .footer-nav{position:absolute;top:775px;left:0;width:1200px;height:20px;font-size:14.2px}
  .footer-nav a{position:absolute;color:#e6e2e8;text-decoration:none}
  .footer-nav .sep{position:absolute;top:8px;width:6px;height:6px;border-radius:50%;background:#6e6a72}
  .sound{position:absolute;left:1112px;top:764px;width:42px;height:42px;border:2px solid #8a878d;border-radius:50%;display:flex;align-items:center;justify-content:center}
</style>
</head>
<body>
  <div class="backdrop" role="img" aria-label="Blurred photo of a dancer in a dim red and purple room"></div>

  <div class="brand"><span class="brand-dot"></span>Velvet Dare</div>

  <h2 class="welcome">Welcome</h2>
  <p class="intro">Before you get started, we need to confirm your age. Our content is intended for a mature audience and is not suitable for individuals under 18.</p>

  <section class="age-check">
    <h1>Are You 18+ Years Old?</h1>
    <div class="choices">
      <button class="choice yes">YES</button>
      <button class="choice no">NO</button>
    </div>
    <p class="notice">
      <svg width="16" height="16" viewBox="0 0 16 16"><circle cx="8" cy="8" r="8" fill="#a9a6ad"/><rect x="7" y="7" width="2" height="5" fill="#000"/><circle cx="8" cy="4.6" r="1.1" fill="#000"/></svg>
      By clicking "Yes", you acknowledge that you are fully aware of the explicit nature of the content provided in Velvet Dare and are of legal age to access it.
    </p>
  </section>

  <nav class="footer-nav">
    <a href="#" style="left:266px">About Us</a>
    <span class="sep" style="left:362px"></span>
    <a href="#" style="left:402px">FAQ</a>
    <span class="sep" style="left:464px"></span>
    <a href="#" style="left:505px">Contact Us</a>
    <span class="sep" style="left:614px"></span>
    <a href="#" style="left:654px">Terms of Service</a>
    <span class="sep" style="left:801px"></span>
    <a href="#" style="left:842px">Privacy Policy</a>
  </nav>

  <div class="sound" aria-label="Sound toggle">
    <svg width="24" height="20" viewBox="0 0 24 20"><path d="M1 7h5l7-6v18l-7-6H1z" fill="#fff"/><rect x="16" y="9" width="5" height="2" fill="#fff"/><rect x="16" y="3.5" width="4" height="2" fill="#fff" transform="rotate(-30 18 4.5)"/><rect x="16" y="14.5" width="4" height="2" fill="#fff" transform="rotate(30 18 15.5)"/></svg>
  </div>
</body>
</html>
```